Professional finish needed to powerpoint slides

I am pitching my business for investment and have two pages as part of the business plan called the 'Quillmarsh Orbit' and the 'Built by the Tollbrook Orbit'.
They are basically visual one page plans to help investors see if the business is worth investing in or not. You only need to take the pages with the diagram in, so 2 pages in total.
The Orbit can be given an edge to make it look info graphic style.
Good luck

```html
<!DOCTYPE html>
<html lang="en">
<head>
<meta charset="utf-8">
<title>Quillmarsh Orbit</title>
<link href="https://fonts.googleapis.com/css2?family=Arimo:wght@400;700&display=swap" rel="stylesheet">
<style>
:root{
  --frame-dark:#2f6e22;
  --frame-light:#5fb04a;
  --sheet:#ffffff;
  --ring-outer:#c9b0e0;
  --ring-inner:#dccbee;
  --ring-line:#f4eefa;
  --spoke:#c23a2e;
  --core:#000000;
  --box-top:#5088c8;
  --box-bottom:#2c5a9a;
  --box-edge:#a9c3e6;
  --label-bg:#050505;
  --text-light:#ffffff;
  --brand-green:#1f6e2c;
}
*{box-sizing:border-box;margin:0;padding:0}
html,body{width:1200px;height:900px;overflow:hidden}
body{
  font-family:"Arimo",Arial,sans-serif;
  background:linear-gradient(180deg,var(--frame-light),var(--frame-dark));
  position:relative;
}
.sheet{position:absolute;left:28px;top:22px;width:1142px;height:856px;background:var(--sheet);overflow:hidden}
.orbit-diagram{position:absolute;left:0;top:0}
.canvas{position:absolute;left:0;top:0;width:1200px;height:900px}
.brand{
  position:absolute;left:56px;top:56px;width:216px;height:90px;
  display:flex;align-items:center;gap:12px;padding-left:14px;
}
.brand-mark{width:22px;height:22px;background:var(--brand-green)}
.brand-name{font-size:34px;font-weight:700;color:var(--brand-green)}
.note{
  position:absolute;display:flex;align-items:center;justify-content:center;text-align:center;
  background:linear-gradient(180deg,var(--box-top),var(--box-bottom));
  border:1px solid var(--box-edge);
  color:var(--text-light);font-size:12px;line-height:1.35;padding:2px 5px;
  box-shadow:2px 2px 3px rgba(0,0,0,.35);
}
.note.soft{background:linear-gradient(180deg,#6a9ed6,#4a7fbe);font-size:15px;line-height:1.3}
.axis-label{
  position:absolute;display:flex;align-items:center;justify-content:center;text-align:center;
  background:var(--label-bg);color:var(--text-light);font-weight:700;font-size:19px;line-height:1.25;
  border:1px solid #555;box-shadow:2px 2px 4px rgba(0,0,0,.45);
}
.year-label{font-size:19px}
</style>
</head>
<body>
<div class="sheet"></div>
<svg class="orbit-diagram" width="1200" height="900" viewBox="0 0 1200 900" aria-hidden="true">
  <defs>
    <radialGradient id="ringFill" cx="50%" cy="50%" r="50%">
      <stop offset="0" stop-color="#e6d8f2"/>
      <stop offset="1" stop-color="#c3a7dc"/>
    </radialGradient>
  </defs>
  <circle cx="668" cy="462" r="420" fill="url(#ringFill)" stroke="#a98cc6" stroke-width="2"/>
  <circle cx="668" cy="462" r="340" fill="none" stroke="var(--ring-line)" stroke-width="3"/>
  <circle cx="668" cy="462" r="262" fill="none" stroke="var(--ring-line)" stroke-width="3"/>
  <circle cx="668" cy="462" r="176" fill="none" stroke="var(--ring-line)" stroke-width="3"/>
  <g stroke="var(--spoke)" stroke-width="4" stroke-linecap="round">
    <line x1="668" y1="462" x2="665" y2="62"/>
    <line x1="668" y1="462" x2="425" y2="98"/>
    <line x1="668" y1="462" x2="890" y2="115"/>
    <line x1="668" y1="462" x2="1000" y2="262"/>
    <line x1="668" y1="462" x2="300" y2="262"/>
    <line x1="668" y1="462" x2="244" y2="462"/>
    <line x1="668" y1="462" x2="1045" y2="640"/>
    <line x1="668" y1="462" x2="895" y2="795"/>
    <line x1="668" y1="462" x2="572" y2="825"/>
    <line x1="668" y1="462" x2="265" y2="634"/>
  </g>
  <circle cx="668" cy="460" r="58" fill="var(--core)"/>
</svg>

<div class="canvas">
  <div class="brand"><span class="brand-mark"></span><span class="brand-name">Quillmarsh</span></div>

  <div class="axis-label" style="left:601px;top:28px;width:128px;height:38px">Net Profit</div>
  <div class="note" style="left:619px;top:82px;width:92px;height:28px">£300k</div>
  <div class="note" style="left:628px;top:165px;width:74px;height:28px">£150k</div>
  <div class="note" style="left:633px;top:260px;width:64px;height:26px">£91k</div>
  <div class="note" style="left:630px;top:334px;width:80px;height:26px">£3,179</div>

  <div class="axis-label" style="left:375px;top:62px;width:100px;height:38px">People</div>
  <div class="note" style="left:416px;top:102px;width:176px;height:62px">Chief Technical Officer, 4 Sales People London/Manchester</div>
  <div class="note" style="left:441px;top:182px;width:184px;height:62px">In house Media x 2, Team – Chirper – 2 Sales People London/Manchester</div>
  <div class="note" style="left:508px;top:284px;width:148px;height:28px">2 Sales Person</div>
  <div class="note" style="left:566px;top:370px;width:134px;height:28px">1 Sales Person</div>

  <div class="axis-label" style="left:880px;top:82px;width:128px;height:38px">Revenue</div>
  <div class="note" style="left:830px;top:146px;width:70px;height:30px">£1m</div>
  <div class="note" style="left:784px;top:220px;width:86px;height:30px">£500k</div>
  <div class="note" style="left:736px;top:282px;width:78px;height:30px">£300k</div>
  <div class="note" style="left:713px;top:338px;width:90px;height:50px">£179,175 (100kSwr)</div>
  <div class="note" style="left:720px;top:390px;width:80px;height:30px">35</div>

  <div class="axis-label" style="left:997px;top:228px;width:144px;height:40px">Subscribers</div>
  <div class="note" style="left:955px;top:272px;width:116px;height:32px">418 @ £299</div>
  <div class="note" style="left:872px;top:310px;width:128px;height:32px">209 @ £299</div>
  <div class="note" style="left:808px;top:346px;width:126px;height:32px">104 @ £299</div>

  <div class="axis-label" style="left:174px;top:202px;width:118px;height:66px">Skills/<br>Training</div>
  <div class="note" style="left:430px;top:334px;width:152px;height:28px">Bring in skills (buy in)</div>
  <div class="note" style="left:430px;top:364px;width:142px;height:84px">Resellers, Franchise, Partners Europe, Manchester, London, Global Markets Pull</div>
  <div class="note" style="left:332px;top:354px;width:94px;height:100px">Consolidate UK, More Global Markets (planned)</div>

  <div class="axis-label" style="left:86px;top:446px;width:156px;height:38px">Operations</div>
  <div class="note soft" style="left:404px;top:456px;width:196px;height:52px">Training Needs Analysis Ad hoc Training</div>
  <div class="note" style="left:304px;top:510px;width:154px;height:76px">Establish “Quillmarsh” Way–Implement, Continually Monitor &amp; Review</div>
  <div class="note" style="left:466px;top:500px;width:192px;height:82px">10-20 plc’s, Visit Website &amp; get 3 contacts on each , run pilot – Mkting, Comms, HR, Fin., MD, Chair</div>
  <div class="note" style="left:672px;top:512px;width:128px;height:60px">Software 56%, (Mng PR, P Blast, 3 Rport Ad – 44%)</div>

  <div class="axis-label year-label" style="left:727px;top:438px;width:74px;height:32px">2013</div>
  <div class="axis-label year-label" style="left:829px;top:438px;width:72px;height:32px">2014</div>
  <div class="axis-label year-label" style="left:918px;top:438px;width:74px;height:32px">2015</div>
  <div class="axis-label year-label" style="left:998px;top:438px;width:80px;height:32px">2016</div>

  <div class="note" style="left:808px;top:482px;width:250px;height:64px">(Avoid PR Market) London/B’ham Tech Govt Corp Suppliers Mkt Global Private Biz</div>
  <div class="note soft" style="left:853px;top:546px;width:178px;height:50px">Develop &amp; Introduce 1 New Product</div>
  <div class="note" style="left:756px;top:582px;width:80px;height:54px">Software 90%, Press Blast 10%</div>
  <div class="note" style="left:845px;top:598px;width:192px;height:82px">Diversification, Agency Market (criteria robust product)Top 100 Companies To Work For</div>

  <div class="axis-label" style="left:131px;top:618px;width:132px;height:34px">Direct Sales</div>
  <div class="note" style="left:270px;top:618px;width:122px;height:32px">As Year 2</div>
  <div class="note" style="left:422px;top:584px;width:336px;height:132px">Webinars, Larkin, Awareness London M’chster, Develop Brand /Val. Prop., Lead Gen. Campaigns, Searchly Ad, e-shots, Target Regions, Mystery Shopping, Online Demos, Introduce A Pro-active Sales Process &amp; Monitoring, Company Product * “In House” Capabilities – Identify Through Media (Research) Database Crest Listed plc’s</div>

  <div class="axis-label" style="left:38px;top:672px;width:218px;height:44px">Objectives</div>
  <div class="axis-label" style="left:1032px;top:638px;width:128px;height:68px">Market<br>Segments</div>
  <div class="note" style="left:775px;top:682px;width:66px;height:26px">100%</div>
  <div class="note" style="left:890px;top:684px;width:140px;height:44px">Planned Evolution with Markets</div>
  <div class="note" style="left:437px;top:718px;width:318px;height:48px">App.,In House Developers, In House Media, Data Control, Social Network, Journalist Bloggers</div>
  <div class="note" style="left:832px;top:750px;width:98px;height:26px">100%</div>
  <div class="axis-label" style="left:900px;top:782px;width:118px;height:66px">Product<br>Mix</div>
  <div class="note" style="left:448px;top:772px;width:268px;height:48px">Review &amp; Continual Adaption Related to Market &amp; New Technologies</div>
  <div class="axis-label" style="left:494px;top:822px;width:146px;height:40px">Marketing</div>
</div>
</body>
</html>
```